Packaging Design job - Health Supplement

We need a packaging design theme for a health supplement for Moroccan consumers. Our product is called 'Velmarine'. https://corvelsante.example/nos-produits/digestion/vel-marine/

It is a unique solution of three plants with recognized benefits. The activated carbon in the product allows, like plants, reduce effectively the problems related to digestion. The product is particularly effective for soothing bloating and optimizing intestinal transit as well as digestion.

We would like to see clean, modern and fresh designs.
This should give the impression of professional products of pharmaceutical quality.

You will find attached the current packaging design of the product. what we do not like:
- The design is not modern
- The design does not evoke the purpose of the product

You will also find attached the logo of our company.

Ps : You can change the color of the logo

Font styles to use
Serif
Sans Serif

Colors

Designer to choose colors to be used in the design.

Requirements
Must have
• - Bottle and box packaging required.
• - Product is bottle of 30 tablets
Should not have
• Sales and other "must buy" "guaranteed" etc

```html
<!DOCTYPE html>
<html lang="fr">
<head>
<meta charset="utf-8">
<title>Vel-Marine — dépliant d'étui</title>
<link href="https://fonts.googleapis.com/css2?family=Fira+Sans:wght@300;400;600&family=Fira+Sans+Condensed:wght@400;500&display=swap" rel="stylesheet">
<style>
  :root{
    --teal:#1aaba7;
    --teal-dark:#13918d;
    --teal-light:#bfe7e5;
    --grey:#8e8e8e;
    --grey-dark:#555;
    --grey-band:#ececec;
    --paper:#ffffff;
    --bg:#eeeeee;
  }
  *{box-sizing:border-box;margin:0;padding:0}
  html,body{width:1200px;height:1200px;overflow:hidden;background:var(--bg)}
  body{position:relative;font-family:"Fira Sans",sans-serif;color:var(--grey)}
  .dieline{position:absolute;left:0;top:0;width:1200px;height:1200px}
  .panel{position:absolute}
  .white{background:var(--paper)}
  .teal{background:linear-gradient(160deg,var(--teal) 0%,var(--teal-dark) 100%)}
  .flap{position:absolute;background:var(--paper)}

  /* top flap */
  .top-flap{left:62px;top:215px;width:375px;height:225px;border-radius:22px 22px 0 0;overflow:hidden}
  .top-flap .band{height:31px;background:var(--teal)}
  .brand{font-family:"Fira Sans",sans-serif;font-weight:600;color:var(--grey);letter-spacing:.5px;display:flex;align-items:center;gap:6px}
  .brand .dot{width:10px;height:10px;border-radius:50%;background:var(--grey)}
  .top-flap .brand{position:absolute;left:110px;top:108px;font-size:20px}

  /* glue strip */
  .glue{left:29px;top:459px;width:33px;height:425px;clip-path:polygon(0 6%,100% 0,100% 100%,0 94%)}

  /* front */
  .front{left:62px;top:440px;width:375px;height:466px;overflow:hidden}
  .front .brand{position:absolute;left:32px;top:34px;font-size:20px}
  .title{position:absolute;font-weight:600;letter-spacing:.5px;white-space:nowrap}
  .title .a{color:var(--teal)}
  .title .b{color:var(--grey)}
  .front .title{left:30px;top:112px;font-size:42px}
  .ingredients{position:absolute;left:0;top:178px;width:375px;height:56px;border-top:1px solid var(--teal);border-bottom:1px solid var(--teal);padding:7px 0 0 30px;font-weight:300;font-size:16px;line-height:20px;color:var(--grey);text-transform:uppercase}
  .ingredients::before{content:"";position:absolute;left:0;top:-1px;width:16px;height:56px;background:var(--teal)}
  .benefits{position:absolute;left:30px;top:264px;list-style:none;font-weight:300;font-size:17px;line-height:22px;color:var(--grey)}
  .benefits li::before{content:"•";color:var(--teal);margin-right:5px}
  .swirl{position:absolute;left:0;top:250px;width:375px;height:216px;background:radial-gradient(ellipse at 85% 55%,rgba(26,171,167,.35),rgba(26,171,167,.08) 55%,rgba(255,255,255,0) 75%)}
  .count{position:absolute;left:30px;bottom:18px;font-family:"Fira Sans Condensed",sans-serif;font-weight:500;font-size:15px;color:var(--teal)}

  /* sides */
  .side{top:440px;width:185px;height:466px;display:flex;align-items:center;justify-content:center;overflow:hidden}
  .side-1{left:437px}
  .side-2{left:990px}
  .side .title{position:static;font-size:40px;color:#fff;letter-spacing:1px}
  .side-1 .title{transform:rotate(-90deg)}
  .side-2 .title{transform:rotate(90deg)}
  .side .sheen{position:absolute;inset:0;background:radial-gradient(ellipse at 20% 20%,rgba(255,255,255,.12),rgba(255,255,255,0) 60%)}

  .tuck{width:174px;height:116px}
  .tuck-up{clip-path:polygon(0 100%,0 22%,10% 0,90% 0,100% 22%,100% 100%)}
  .tuck-down{clip-path:polygon(0 0,100% 0,100% 100%,88% 100%,82% 40%,18% 40%,12% 100%,0 100%)}

  /* back */
  .back{left:621px;top:440px;width:369px;height:466px;overflow:hidden;font-size:11.5px;line-height:15.5px}
  .back::before{content:"";position:absolute;left:0;top:60px;width:12px;height:212px;background:var(--teal)}
  .back .brand{position:absolute;right:30px;top:30px;font-size:16px}
  .back .brand .dot{width:8px;height:8px}
  .back h2{position:absolute;left:38px;top:60px;font-family:"Fira Sans Condensed",sans-serif;font-weight:500;font-size:15px;color:var(--teal);letter-spacing:.3px}
  .back .intro{position:absolute;left:38px;top:88px;width:300px;font-weight:300;color:var(--grey)}
  .back .boxed{position:absolute;left:25px;top:205px;width:344px;height:72px;background:var(--grey-band);padding:8px 30px 0 13px;font-weight:300;color:var(--grey)}
  .back .lead{position:absolute;left:38px;top:330px;width:300px;font-family:"Fira Sans Condensed",sans-serif;font-weight:500;font-size:13px;line-height:17px;color:var(--teal)}
  .back .info{position:absolute;left:38px;top:372px;font-family:"Fira Sans Condensed",sans-serif;font-size:12.5px;line-height:20px;color:var(--grey-dark)}
  .back .info .url{font-family:"Fira Sans",sans-serif;font-weight:300;color:var(--grey)}
</style>
</head>
<body>
<main class="dieline">
  <div class="flap top-flap">
    <div class="band"></div>
    <div class="brand"><span class="dot"></span>CORVELSANTÉ</div>
  </div>

  <div class="panel glue teal"></div>

  <section class="panel front white">
    <div class="brand"><span class="dot"></span>CORVELSANTÉ</div>
    <div class="swirl" role="img" aria-label="Vagues fluides turquoise en fond"></div>
    <h1 class="title"><span class="a">VEL-</span><span class="b">MARINE</span></h1>
    <p class="ingredients">Fenouil - Anis vert - Carvi noir<br>Charbon végétal active</p>
    <ul class="benefits">
      <li>Facilite le transit</li>
      <li>Améliore la digestion</li>
      <li>Effet ventre plat</li>
    </ul>
    <p class="count">30 Gélules</p>
  </section>

  <div class="flap tuck tuck-up" style="left:446px;top:324px"></div>
  <section class="panel side side-1 teal"><div class="sheen"></div><span class="title">VEL-MARINE</span></section>
  <div class="flap tuck tuck-down" style="left:446px;top:906px"></div>

  <section class="panel back white">
    <div class="brand"><span class="dot"></span>CORVELSANTÉ</div>
    <h2>PROPRIÉTÉS</h2>
    <p class="intro">l'association unique du<br>Lorem Ipsum is simply dummy text of the printing and typesetting industry. Lorem Ipsum has been the industry's standard dummy text ever since the 1500s, when an unknown printer took a galley of type and scrambled it to make a type specimen book.</p>
    <p class="boxed">Lorem Ipsum has been the industry's standard dummy text ever since the 1500s, when an unknown printer took a galley of type and scrambled it to make a type specimen book.</p>
    <p class="lead">Contrary to popular belief, Lorem Ipsum is not simply random text.</p>
    <p class="info">Fahriqué on France<br>Distribue Par : CORVELSANTÉ - NORVANE<br><span class="url">www.corvelsante.example</span></p>
  </section>

  <div class="flap tuck tuck-up" style="left:1000px;top:324px"></div>
  <section class="panel side side-2 teal"><div class="sheen"></div><span class="title">VEL-MARINE</span></section>
  <div class="flap tuck tuck-down" style="left:1000px;top:906px"></div>
</main>
</body>
</html>
```